Circular Wedding Menu Design - Adobe Illustrator

I am looking for a design for circular wedding menus. these will be 7 inches.I'm providing a template from the printer, AI files of our wedding invitation, and the menu items.

The paper our invitations were printed on was a sandy beige color. please make the background for this the same color. It will be put ontop of a white plate with ivory tablecloth and cappucino covered napkins.

IMPORTANT - We aren't committed to a specific design so feel free to use whatever you like, but we definitely want the cow, fish, and carrot images from our rsvp to be used for the entrees in the menu.

IMPORTANT - must be in Adobe illustrator format

for inspiration:
http://cdn.velvorabridalnotes.example/wp-content/uploads/2012/10/tormane-styled-19.jpg

http://www.quorbelsearch.example/imgres?imgurl=http%3A%2F%2Fwww.dellivanestudio.example%2Fblog%2Fwp-content%2Fuploads%2F2013%2F07%2FPetal-Ledger-Round-Menu-Wedding-Place-Setting.jpg&imgrefurl=http%3A%2F%2Fwww.dellivanestudio.example%2Fblog%2Finspiration%2Fsimply-lovely-wedding-menu-place-settings%2F&h=815&w=600&tbnid=8kRqzp_4LUTWEN%3A&zoom=1&docid=72HJKs9PqMxaTN&ei=QwERtYu8LpMsoBF2xdDTRk&tbm=isch&ved=0DHtRNzhKNBk&iact=rc&uact=3&dur=526&page=1&start=0&ndsp=30

https://thumbs3.pixorvane.example/images?q=tbn:QWe7KpLmNvBxRtYu2Hs4DfGhJkZxCvBnMqWeRtYuIoPaSdFgHjK

https://thumbs3.pixorvane.example/images?q=tbn:ZxC8vBnMqW_e42RT_yUioPaSdFgHjKlZxCv66BnM7q_WERtyUiOp

https://thumbs2.pixorvane.example/images?q=tbn:LkJh5GfDsAp9OiUyTrEwQ-MNbV8cXzL3KjHgFdsaPoIuYtReW0Q

Industry/Entity Type

Wedding

```html
<!DOCTYPE html>
<html lang="en">
<head>
<meta charset="utf-8">
<title>Wedding Menu</title>
<link rel="stylesheet" href="https://fonts.googleapis.com/css2?family=Aleo:wght@300;400;600&display=swap">
<style>
  :root {
    --page: #ffffff;
    --frame: #2b2b2b;
    --sand: #dbcfb5;
    --ink: #85878a;
    --gold: #b8902a;
    --vine-dark: #a7a398;
    --vine-light: #cdc4ae;
  }
  html, body {
    margin: 0;
    width: 1200px;
    height: 1000px;
    overflow: hidden;
    background: var(--page);
  }
  .canvas {
    position: relative;
    width: 1200px;
    height: 1000px;
    font-family: "Aleo", Georgia, serif;
    color: var(--ink);
  }
  .frame {
    position: absolute;
    left: 18px; top: 16px;
    width: 1152px; height: 952px;
    border: 6px solid var(--frame);
  }
  .menu-disc {
    position: absolute;
    left: 164px; top: 60px;
    width: 880px; height: 880px;
    border-radius: 50%;
    background: var(--sand);
  }
  .vines {
    position: absolute;
    left: 0; top: 0;
    width: 1200px; height: 1000px;
  }
  .block {
    position: absolute;
    left: 164px;
    width: 880px;
    text-align: center;
    margin: 0;
  }
  .menu-title {
    top: 274px;
    font-size: 76px;
    font-weight: 400;
    line-height: 88px;
    letter-spacing: 1px;
  }
  .course-heading {
    display: flex;
    justify-content: center;
    align-items: center;
    gap: 14px;
    font-size: 19px;
    font-weight: 600;
    line-height: 24px;
  }
  .course-heading::before,
  .course-heading::after {
    content: "";
    width: 58px;
    height: 2px;
    background: var(--gold);
  }
  .dish {
    font-size: 18.5px;
    font-weight: 400;
    line-height: 22px;
  }
  .entree-mark {
    position: absolute;
    left: 589px;
    width: 32px;
    height: 30px;
    border-radius: 6px;
    background: var(--gold);
  }
  .couple {
    color: var(--gold);
    font-size: 17px;
    line-height: 20px;
  }
  .date {
    font-size: 16px;
    line-height: 20px;
  }
</style>
</head>
<body>
<div class="canvas">
  <div class="frame"></div>
  <div class="menu-disc"></div>

  <svg class="vines" viewBox="0 0 1200 1000" role="img" aria-label="Hand-drawn leafy vine branches arching over the menu title">
    <defs>
      <clipPath id="disc-clip"><circle cx="604" cy="500" r="440"/></clipPath>
      <linearGradient id="vine-tone" x1="0" y1="0" x2="1" y2="1">
        <stop offset="0" stop-color="var(--vine-dark)" stop-opacity="0.55"/>
        <stop offset="1" stop-color="var(--vine-light)" stop-opacity="0.7"/>
      </linearGradient>
    </defs>
    <g clip-path="url(#disc-clip)" fill="url(#vine-tone)">
      <path d="M604,150 C520,108 330,140 266,290 L270,402 L304,404 C318,300 420,192 604,170 Z"/>
      <path transform="translate(1208,0) scale(-1,1)" d="M604,150 C520,108 330,140 266,290 L270,402 L304,404 C318,300 420,192 604,170 Z"/>
    </g>
  </svg>

  <h1 class="block menu-title">MENU</h1>

  <h2 class="block course-heading" style="top:373px">Salad</h2>
  <p class="block dish" style="top:397px">Grilled Watermelon &amp; Fig Salad: Gem Lettuces, Watermelon, Figs,<br>Toasted Hazelnuts, Balsamic Reduction, Honey-Orange Dressing</p>

  <h2 class="block course-heading" style="top:466px">Entrée</h2>

  <div class="entree-mark" style="top:500px" role="img" aria-label="Cow icon for the beef entrée"></div>
  <p class="block dish" style="top:535px">Roasted Filet Mignon, Wild Mushrooms, Garlic Mashed<br>Potatoes, Asparagus with Red Wine Sauce</p>

  <div class="entree-mark" style="top:591px" role="img" aria-label="Fish icon for the fish entrée"></div>
  <p class="block dish" style="top:624px">Porcini Crusted Halibut, Lemon-Herb Potatoes,<br>Black Kale, Early Girl Tomatoes</p>

  <div class="entree-mark" style="top:675px" role="img" aria-label="Carrot icon for the vegetarian entrée"></div>
  <p class="block dish" style="top:713px">Artichoke Agnolotti, Wild Mushrooms, Baby Arugula,<br>Goat Cheese, White Wine Sauce, Micro herbs</p>

  <h2 class="block course-heading" style="top:779px">Wedding Cake</h2>
  <p class="block dish" style="top:803px">Delicate Butter Pecan With Fresh Raspberry Mouse</p>

  <p class="block couple" style="top:857px">Mirela Ostrova &amp; Daniel Keshet</p>
  <p class="block date" style="top:877px">June 21, 2014</p>
</div>
</body>
</html>
```